New Business Card Design Project VORASTI-Italy

we are VORASTI-Italy
our company in the market for 3 years we are luxury cosmetic company and its about time for a facelift :)
i will like to have elegant luxurious and unique business card
that will give the person that get it a unique, luxurious and elegant impression
I'm VERY OPEN FOR NEW IDEAS , even duo i add a few files of things that i see on line and i like them

i add my logo as well
my website is VORASTI.COM
(if you would like to see the main style that we have)

Target Market(s)

adult that have money :)

Industry/Entity Type

Business

Contact Information for Business Card

Name - Paul Vorasti
Position - CEO and CO Founder
address - 4817 E Larkdale
telephone - 555-384-1962
email - paul@vorasti.com
fax - 555-384-1962
website - VORASTI.COM

Colors
000000
959595
fbee3e
ffffff

Requirements
Must have
• big logo in GOLD color
• elegant look
• impressive
Nice to have
• not must but maybe classy pattern background
• not must but maybe emblem
• maybe clear plastic business card
Should not have
• colors
• images

```html
<!DOCTYPE html>
<html lang="en">
<head>
<meta charset="utf-8">
<title>VORASTI-Italy Business Card</title>
<link rel="stylesheet" href="https://fonts.googleapis.com/css2?family=Montserrat:wght@500;700&family=Cinzel:wght@400&display=swap">
<style>
  :root {
    --page: #ffffff;
    --ink: #000000;
    --card-dark: #141414;
    --card-mid: #1e1f1f;
    --gold: #d4ae4a;
    --gold-light: #e2c062;
    --gold-deep: #6e4a1c;
    --band-dark: #3a1c08;
    --band-olive: #8c9440;
    --white: #ffffff;
  }
  * { margin: 0; padding: 0; box-sizing: border-box; }
  html, body { width: 1200px; height: 1200px; overflow: hidden; background: var(--page); }
  .canvas { position: relative; width: 1200px; height: 1200px; }

  .card {
    position: absolute;
    left: 180px;
    width: 840px;
    height: 480px;
    overflow: hidden;
  }
  .card--front { top: 87px; }
  .card--back { top: 633px; }

  .damask-field {
    position: absolute;
    inset: 0;
    background: radial-gradient(ellipse at 50% 55%, var(--card-mid) 0%, var(--card-dark) 60%, #0a0a0a 100%);
  }

  .holder-name {
    position: absolute;
    top: 97px;
    width: 100%;
    text-align: center;
    font-family: "Montserrat", sans-serif;
    font-weight: 700;
    font-size: 54px;
    line-height: 64px;
    color: var(--white);
  }
  .holder-role {
    position: absolute;
    top: 155px;
    width: 100%;
    text-align: center;
    font-family: "Montserrat", sans-serif;
    font-weight: 500;
    font-size: 21px;
    letter-spacing: 0.5px;
    color: var(--white);
  }

  .accent-band {
    position: absolute;
    top: 331px;
    left: 0;
    width: 100%;
    height: 27px;
    background: linear-gradient(90deg, var(--band-dark) 0%, #5a3010 8%, var(--band-olive) 20%, #6e4a1e 32%, #5e3812 50%, #6e4a1e 68%, var(--band-olive) 80%, #5a3010 92%, var(--band-dark) 100%);
  }
  .contact-panel {
    position: absolute;
    top: 358px;
    left: 0;
    width: 100%;
    height: 122px;
    background: radial-gradient(ellipse 55% 120% at 50% 10%, var(--gold-light) 0%, var(--gold) 45%, #a47c30 75%, var(--gold-deep) 100%);
  }
  .contact-item {
    position: absolute;
    display: flex;
    align-items: center;
    gap: 9px;
    font-family: "Montserrat", sans-serif;
    font-weight: 500;
    font-size: 18px;
    color: #111;
    white-space: nowrap;
  }
  .contact-item svg { width: 24px; height: 24px; flex: none; }
  .contact-item--address { left: 96px; top: 18px; }
  .contact-item--email { left: 96px; top: 44px; }
  .contact-item--phone { left: 572px; top: 17px; }
  .contact-item--fax { left: 572px; top: 47px; }
  .contact-item--web { left: 320px; top: 85px; }

  .emblem-ring {
    position: absolute;
    left: 313px;
    top: 29px;
    width: 214px;
    height: 214px;
    border-radius: 50%;
    border: 5px solid var(--gold);
  }
  .brand-name {
    position: absolute;
    top: 272px;
    width: 100%;
    text-align: center;
    font-family: "Cinzel", serif;
    font-weight: 400;
    font-size: 92px;
    line-height: 110px;
    color: var(--gold);
  }
  .brand-rule {
    position: absolute;
    top: 397px;
    left: 184px;
    width: 472px;
    height: 4px;
    background: var(--gold);
  }
  .brand-origin {
    position: absolute;
    top: 416px;
    width: 100%;
    text-align: center;
    font-family: "Cinzel", serif;
    font-weight: 400;
    font-size: 35px;
    color: var(--gold);
  }
</style>
</head>
<body>
<main class="canvas">

  <section class="card card--front">
    <div class="damask-field" role="img" aria-label="Dark black damask ornamental pattern background"></div>
    <h1 class="holder-name">Paul Vorasti</h1>
    <p class="holder-role">CEO and CO Founder</p>
    <div class="accent-band"></div>
    <div class="contact-panel">
      <p class="contact-item contact-item--address">
        <svg viewBox="0 0 24 24"><path d="M12 2a7 7 0 0 0-7 7c0 5 7 13 7 13s7-8 7-13a7 7 0 0 0-7-7zm0 9.5A2.5 2.5 0 1 1 12 6.5a2.5 2.5 0 0 1 0 5z" fill="#111"/></svg>
        4817 E Larkdale
      </p>
      <p class="contact-item contact-item--email">
        <svg viewBox="0 0 24 24"><rect x="2" y="5" width="20" height="14" rx="1" fill="none" stroke="#111" stroke-width="2"/><path d="M2 6l10 7 10-7" fill="none" stroke="#111" stroke-width="2"/></svg>
        paul@vorasti.com
      </p>
      <p class="contact-item contact-item--phone">
        <svg viewBox="0 0 24 24"><rect x="6" y="2" width="12" height="20" rx="2" fill="none" stroke="#111" stroke-width="2"/><circle cx="12" cy="18" r="1.2" fill="#111"/></svg>
        555-384-1962
      </p>
      <p class="contact-item contact-item--fax">
        <svg viewBox="0 0 24 24"><rect x="2" y="7" width="5" height="15" rx="1" fill="#111"/><rect x="8" y="9" width="14" height="13" rx="1" fill="#111"/><rect x="10" y="2" width="9" height="7" fill="none" stroke="#111" stroke-width="1.6"/><g fill="#d4ae4a"><rect x="10" y="13" width="2" height="2"/><rect x="14" y="13" width="2" height="2"/><rect x="18" y="13" width="2" height="2"/><rect x="10" y="17" width="2" height="2"/><rect x="14" y="17" width="2" height="2"/><rect x="18" y="17" width="2" height="2"/></g></svg>
        555-384-1962
      </p>
      <p class="contact-item contact-item--web">
        <svg viewBox="0 0 24 24"><circle cx="12" cy="12" r="10" fill="#111"/><path d="M7 8c2-1 3 1 4 2s-1 3 1 4 1 4 0 5M14 5c1 2 3 2 4 4" fill="none" stroke="#d4ae4a" stroke-width="1.6"/></svg>
        WWW.VORASTI.COM
      </p>
    </div>
  </section>

  <section class="card card--back">
    <div class="damask-field" role="img" aria-label="Dark black damask ornamental pattern background"></div>
    <div class="emblem-ring"></div>
    <p class="brand-name">VORASTI</p>
    <div class="brand-rule"></div>
    <p class="brand-origin">ITALY</p>
  </section>

</main>
</body>
</html>
```